Ad design for a macarons brand

We are a dessert brand with one product line: macarons. Our products delight. Every bite is a dream!

We are launching a new product and would like to lunch a small tactical campaign for the product to boost sales.

The new macron is mango ganache and the middle a mix of sour mango and yuzu (https://www.plumvarell.com/about-the-fruit-584302).

Here are some images we took of the new macaron
https://www.fennlocker.com/sh/qrtwpzhkvbmls/AAFJtRWD-nxPlkhQZ7CeW4DLp?dl=0

I attach the brand guideline document.

Required sizes

1080 x 1350
1080 x 1920

```html
<!DOCTYPE html>
<html lang="en">
<head>
<meta charset="utf-8">
<title>Mango – Latest Flavour by Velour</title>
<link rel="stylesheet" href="https://fonts.googleapis.com/css2?family=Archivo:wght@600&family=Barlow:wght@300;600&family=Cormorant+Garamond:wght@500&display=swap">
<style>
  :root {
    --sun-yellow: #ffec2a;
    --sun-yellow-deep: #fdd424;
    --mango-orange: #f5a300;
    --footer-orange: #ee9a1c;
    --paper: #ffffff;
    --macaron-light: #f6b347;
    --macaron-mid: #e89a2e;
    --macaron-deep: #d98420;
  }
  html, body {
    margin: 0;
    padding: 0;
    width: 1200px;
    height: 960px;
    overflow: hidden;
    background: var(--paper);
  }
  .ad {
    position: relative;
    width: 1200px;
    height: 960px;
    background: var(--paper);
    overflow: hidden;
  }
  .hero-band {
    position: absolute;
    left: 0;
    top: 0;
    width: 1200px;
    height: 811px;
    background: linear-gradient(100deg, var(--sun-yellow) 0%, var(--sun-yellow) 55%, var(--sun-yellow-deep) 100%);
  }
  .macaron-stack {
    position: absolute;
    left: 817px;
    top: 0;
    width: 254px;
    height: 875px;
    border-radius: 0 0 120px 120px / 0 0 50px 50px;
    background:
      linear-gradient(90deg, rgba(0,0,0,0.08) 0%, rgba(255,255,255,0.10) 45%, rgba(0,0,0,0.10) 100%),
      linear-gradient(180deg, var(--macaron-light) 0%, var(--macaron-mid) 50%, var(--macaron-deep) 100%);
    box-shadow: 30px 10px 40px rgba(180, 110, 0, 0.18);
  }
  .headline {
    position: absolute;
    left: 78px;
    top: 300px;
    margin: 0;
    font-family: "Archivo", sans-serif;
    font-weight: 600;
    font-size: 256px;
    line-height: 1;
    letter-spacing: 2px;
    color: var(--paper);
  }
  .tagline {
    position: absolute;
    left: 84px;
    top: 541px;
    margin: 0;
    font-family: "Barlow", sans-serif;
    font-weight: 600;
    font-size: 38px;
    line-height: 1;
    letter-spacing: -0.5px;
    color: var(--mango-orange);
  }
  .tagline .accent {
    color: var(--paper);
  }
  .signoff {
    position: absolute;
    left: 82px;
    top: 862px;
    display: flex;
    align-items: center;
    gap: 26px;
  }
  .signoff-label {
    font-family: "Barlow", sans-serif;
    font-weight: 300;
    font-size: 21px;
    color: var(--footer-orange);
  }
  .brand-name {
    font-family: "Cormorant Garamond", serif;
    font-weight: 500;
    font-size: 42px;
    line-height: 1;
    color: var(--footer-orange);
    letter-spacing: 1px;
  }
</style>
</head>
<body>
  <main class="ad">
    <div class="hero-band"></div>
    <div class="macaron-stack" role="img" aria-label="Vertical stack of six orange mango macarons with yellow mango-yuzu filling"></div>
    <h1 class="headline">MANGO</h1>
    <p class="tagline">NEVER GOES OUT OF <span class="accent">STYLE</span></p>
    <footer class="signoff">
      <span class="signoff-label">LATEST FLAVOUR BY</span>
      <span class="brand-name">VELOUR</span>
    </footer>
  </main>
</body>
</html>
```